Proposal Form

Hello! We would like a full color (CMYK) form created with our logo and a similar look and feel to other documents we use (attached). Underneath logo and some design (design should be landscaping based as that is what we will be quoting), we would need a bunch of horizontal lines (for us to write on) and a space in the bottom right which has three lines - (1) Project Total _____________ (2) ______ Monthly Payments of _________________ (3) Pre-pay and receive a 3% discount _______________________

```html
<!DOCTYPE html>
<html lang="en">
<head>
<meta charset="utf-8">
<title>Maple Ridge Landscaping – Snowplowing Proposal</title>
<link rel="stylesheet" href="https://fonts.googleapis.com/css2?family=Ubuntu:wght@400;500&family=Exo+2:wght@800&family=Arimo&display=swap">
<style>
  :root{
    --ink:#1b1b1d;
    --white:#ffffff;
    --green:#2fb45a;
    --blue:#5a9fd6;
    --rule:#3a3a3a;
    --gold:#d9b23a;
    --badge-green:#3a9a4e;
    --teal:#2a8a5e;
  }
  *{box-sizing:border-box;margin:0;padding:0}
  html,body{width:928px;height:1200px;overflow:hidden;background:var(--white)}
  .sheet{position:relative;width:928px;height:1200px;overflow:hidden;font-family:"Ubuntu",sans-serif;color:var(--ink)}
  .backdrop{position:absolute;inset:0}

  .brand{position:absolute;left:50px;top:78px;color:var(--white)}
  .brand-name{font-size:38px;letter-spacing:9px;text-transform:uppercase;line-height:1}
  .brand-sub{font-size:12px;letter-spacing:15px;text-transform:uppercase;margin-top:18px;padding-left:64px}

  .contact{position:absolute;left:48px;top:158px;color:var(--white);font-size:19px;line-height:24px;font-style:normal}

  .client-card{position:absolute;left:453px;top:42px;width:447px;height:182px;background:var(--white);
    border-radius:4px 34px 4px 34px;padding:16px 23px 0 27px}
  .field{display:flex;align-items:flex-end;height:30.5px;font-size:16.5px}
  .field .blank{flex:1;border-bottom:1.3px solid var(--ink);margin-left:6px;margin-bottom:4px}
  .field .blank.city{flex:0 0 220px;margin-left:18px;margin-right:14px}
  .field .blank.zip{flex:1}

  .photo{position:absolute;border-radius:50%;border:3px solid var(--green);
    background:radial-gradient(circle at 45% 40%,#f4f6f8 0%,#cfd5db 45%,#6d7278 80%,#3b3e42 100%)}
  .photo-one{left:107px;top:299px;width:158px;height:158px}
  .photo-two{left:279px;top:255px;width:187px;height:187px}

  .service-tab{position:absolute;left:474px;top:362px;width:406px;height:83px;background:var(--ink);
    border-radius:34px 16px 0 0;display:flex;align-items:center;justify-content:center}
  .service-title{font-family:"Exo 2",sans-serif;font-weight:800;font-size:43px;color:var(--green);letter-spacing:0;line-height:1}

  .writing-lines{position:absolute;left:91px;top:516px;width:744px;list-style:none}
  .writing-lines li{height:59.1px;border-top:1.2px solid var(--rule)}

  .totals{position:absolute;left:314px;top:1018px;width:519px;font-family:"Arimo",sans-serif;font-size:19.5px}
  .total-row{display:flex;align-items:flex-end;height:35px}
  .total-row .blank{border-bottom:1.3px solid var(--ink);margin-bottom:4px}
  .total-row .grow{flex:1;margin-left:7px}
  .total-row .short{width:64px;margin:0 7px}
</style>
</head>
<body>
<main class="sheet">
  <svg class="backdrop" width="928" height="1200" viewBox="0 0 928 1200" aria-hidden="true">
    <path d="M0 0H928V332C700 300 560 318 420 328 300 338 150 320 0 288Z" fill="var(--ink)"/>
    <path d="M0 290C140 318 290 336 420 328 560 320 720 300 928 334V340C720 308 560 326 420 334 290 342 140 326 0 302Z" fill="var(--blue)"/>
    <rect x="58" y="386" width="812" height="771" rx="48" fill="none" stroke="var(--green)" stroke-width="5"/>
    <rect x="71" y="398" width="786" height="745" rx="38" fill="none" stroke="var(--green)" stroke-width="2.5"/>
    <g class="badges">
      <circle cx="542" cy="292" r="30" fill="var(--gold)"/>
      <circle cx="621" cy="290" r="30" fill="var(--gold)"/>
      <circle cx="706" cy="292" r="30" fill="var(--badge-green)"/>
      <circle cx="798" cy="292" r="30" fill="var(--teal)"/>
    </g>
  </svg>

  <header class="brand">
    <div class="brand-name">Maple Ridge</div>
    <div class="brand-sub">Landscaping</div>
  </header>

  <address class="contact">
    1480 Birchwood Lane NE<br>
    Willow Bend, MI 49000<br>
    Ph: (555) 214-7730<br>
    Email: office@mapleridgeland.com
  </address>

  <section class="client-card">
    <div class="field">Name<span class="blank"></span></div>
    <div class="field">Address<span class="blank"></span></div>
    <div class="field">Phone<span class="blank"></span></div>
    <div class="field">City<span class="blank city"></span>Zip<span class="blank zip"></span></div>
    <div class="field">Email Address<span class="blank"></span></div>
  </section>

  <div class="photo photo-one" role="img" aria-label="Photo of a pickup truck pushing snow with a white plow blade"></div>
  <div class="photo photo-two" role="img" aria-label="Photo of a white truck with a yellow snowplow clearing a snowy road"></div>

  <div class="service-tab"><h1 class="service-title">SNOWPLOWING</h1></div>

  <ul class="writing-lines">
    <li></li><li></li><li></li><li></li><li></li><li></li><li></li><li></li><li></li>
  </ul>

  <section class="totals">
    <div class="total-row">(1) Project Total<span class="blank grow"></span></div>
    <div class="total-row">(2)<span class="blank short"></span>Monthly Payments of<span class="blank grow"></span></div>
    <div class="total-row">(3) Pre-pay and receive a 3% discount<span class="blank grow"></span></div>
  </section>
</main>
</body>
</html>
```